Apply Existing Website Design to Pellmoor-Made Tele-Wellness App (UX/UI Work)

We’re looking for a highly skilled UX/UI designer to translate our existing website design into an intuitive, beautiful mobile app interface for our Pellmoor-developed tele-wellness platform. Hoping this designer will stay onboard with us for future work.

Scope of Work:
    •    Review our existing website design (style, colors, typography, components)
    •    Apply the same visual language to our mobile app screens
    •    Ensure consistent, user-friendly experience across the app
    •    Deliver high-fidelity mockups and design assets (preferably in Figma)
    •    Minimal UX rethinking may be needed to optimize for mobile, but the core brand and design system are already established

What We Provide:
    •    Access to the existing website design (including any style guides or component libraries)
    •    Wireframes or a basic functional map of the app screens
    •    Clear guidelines on branding and user flows

Ideal Candidate:
    •    Strong portfolio of mobile app design, especially healthcare/wellness preferred
    •    Proven experience in adapting web designs for mobile apps
    •    Expertise with Figma or comparable tools
    •    Attention to detail and commitment to brand consistency
    •    Ability to deliver quickly while maintaining quality

Deliverables:
    •    Complete set of high-fidelity, mobile-optimized app screens
    •    Organized design file (Figma preferred) ready for developer handoff
    •    Design assets as needed (icons, images, components)

Timeline:
    •    Estimated 1 week for initial delivery, with room for revisions

```html
<!DOCTYPE html>
<html lang="en">
<head>
<meta charset="UTF-8">
<title>Verda – Tele-Wellness</title>
<link href="https://fonts.googleapis.com/css2?family=Lato:wght@400;700;900&family=Poppins:wght@400;500&display=swap" rel="stylesheet">
<style>
  :root {
    --stage: #000000;
    --screen: #ffffff;
    --leaf: #86b63a;
    --leaf-deep: #6f9e22;
    --leaf-light: #a3c957;
    --blossom: #eef3ee;
    --ink: #333333;
    --ink-soft: #555555;
    --ink-muted: #8a8a8a;
    --white: #ffffff;
    --lilac: #eadcff;
    --lilac-ink: #4a2d7a;
    --peach: #fdd3a8;
  }
  * { box-sizing: border-box; margin: 0; padding: 0; }
  html, body { width: 1200px; height: 753px; overflow: hidden; background: var(--stage); }
  .app-screen {
    position: absolute; left: 430px; top: 0;
    width: 340px; height: 753px; overflow: hidden;
    background: var(--screen);
    font-family: "Lato", sans-serif;
  }
  .app-header {
    position: absolute; left: 0; top: 0; width: 100%; height: 70px;
    background: linear-gradient(90deg, var(--leaf-light) 0%, #b9d77a 60%, var(--blossom) 85%);
  }
  .brand {
    position: absolute; left: 38px; top: 17px;
    font-family: "Lato", sans-serif; font-weight: 900; font-size: 21px;
    letter-spacing: 1.5px; color: var(--white);
  }
  .menu-icon { position: absolute; right: 28px; top: 25px; }
  .hero {
    position: absolute; left: 0; top: 70px; width: 100%; height: 293px;
  }
  .hero-photo {
    position: absolute; inset: 0;
    background: linear-gradient(100deg, var(--leaf-deep) 0%, var(--leaf) 45%, #c9dcc0 68%, var(--blossom) 82%, #dfe8d8 100%);
  }
  .hero-copy { position: absolute; left: 31px; top: 33px; }
  .hero-title {
    font-weight: 700; font-size: 24px; line-height: 25px; color: var(--ink);
  }
  .hero-lines { margin-top: 10px; color: var(--white); font-weight: 700; font-size: 13px; }
  .hero-lines p { line-height: 25px; }
  .hero-origin { margin-top: 27px; color: var(--white); font-weight: 700; font-size: 13px; }
  .book-button {
    position: absolute; left: 32px; top: 225px;
    width: 112px; height: 33px; border-radius: 17px;
    background: var(--lilac); color: var(--lilac-ink);
    font-family: "Poppins", sans-serif; font-weight: 500; font-size: 11px; letter-spacing: .3px;
    display: flex; align-items: center; justify-content: center; gap: 7px;
  }
  .trust { position: absolute; left: 31px; top: 380px; }
  .trust-title { font-size: 20px; color: var(--ink-soft); font-weight: 400; }
  .trust-title strong { font-weight: 700; }
  .trust-sub { font-size: 12.5px; color: var(--ink-muted); margin-top: 1px; }
  .testimonial {
    position: absolute; top: 449px; width: 238px; height: 238px;
    border-radius: 50%; background: var(--peach);
  }
  .testimonial.side-left { left: -215px; }
  .testimonial.side-right { left: 304px; }
  .testimonial.featured {
    left: 50px; text-align: center;
    font-family: "Poppins", sans-serif; color: var(--ink);
  }
  .avatar {
    position: absolute; left: 100px; top: 29px; width: 38px; height: 38px;
    border-radius: 50%; background: linear-gradient(160deg, #c9d3dc, #7a8ea3);
    border: 2px solid var(--white);
  }
  .role { position: absolute; top: 74px; width: 100%; font-size: 10px; font-weight: 500; line-height: 15px; }
  .quote {
    position: absolute; top: 108px; left: 22px; width: 194px;
    font-size: 8.6px; line-height: 14px; color: var(--ink-soft);
  }
  .author { position: absolute; top: 220px; width: 100%; font-size: 8.6px; color: var(--ink-soft); }
  .results { position: absolute; left: 30px; top: 714px; }
  .results-title { font-size: 20px; font-weight: 700; color: var(--ink-soft); }
  .results-sub { font-size: 12.5px; color: var(--ink-muted); margin-top: 4px; }
</style>
</head>
<body>
  <main class="app-screen">
    <header class="app-header">
      <div class="brand">VERDA</div>
      <svg class="menu-icon" width="16" height="12" viewBox="0 0 16 12" aria-label="Menu">
        <rect y="0" width="16" height="2" fill="#333"/>
        <rect y="5" width="16" height="2" fill="#333"/>
        <rect y="10" width="16" height="2" fill="#333"/>
      </svg>
    </header>

    <section class="hero">
      <div class="hero-photo" role="img" aria-label="Close-up photo of white blossoms against a soft green background"></div>
      <div class="hero-copy">
        <h1 class="hero-title">Holistic - Doctor like care<br>Pay as you like</h1>
        <div class="hero-lines">
          <p>Evidence based care with heart.</p>
          <p>Tailored only for you,</p>
          <p>Telle- Wellness</p>
        </div>
        <p class="hero-origin">Developed at Pellmoor</p>
      </div>
      <div class="book-button">
        <svg width="14" height="14" viewBox="0 0 14 14" aria-hidden="true">
          <circle cx="7" cy="7" r="6" fill="none" stroke="#4a2d7a" stroke-width="1.3"/>
          <polygon points="7,3.4 7.9,5.9 10.5,5.9 8.4,7.5 9.2,10 7,8.5 4.8,10 5.6,7.5 3.5,5.9 6.1,5.9" fill="#4a2d7a"/>
        </svg>
        BOOK NOW
      </div>
    </section>

    <section class="trust">
      <h2 class="trust-title">Trusted by <strong>- Northfield Outfitters</strong></h2>
      <p class="trust-sub">Pioneer in corporate wellness, way to Grow</p>
    </section>

    <div class="testimonial side-left"></div>
    <article class="testimonial featured">
      <div class="avatar" role="img" aria-label="Portrait photo of the reviewer"></div>
      <p class="role">Chief Strategy Officer,<br>National Tech Firm</p>
      <p class="quote">For the first time in 20 years of nonstop output, I found a wellness system that didn't just slow me down—it woke me up. Verda's personalized protocols gave me energy I didn't know I was missing, and helped me show up sharper, calmer, and more focused than ever before.</p>
      <p class="author">Marcus</p>
    </article>
    <div class="testimonial side-right"></div>

    <section class="results">
      <h2 class="results-title">Time Tested &amp; Results Driven</h2>
      <p class="results-sub">We get it.. Its for something real- and built</p>
    </section>
  </main>
</body>
</html>
```